could someone please design some snazzy business cards for "Tidy Meadow"
the website is tidymeadow.co.nz

the logo is attached

name : Harriet Osbrook
Contact Number: 0224819357
email: harrietosb@tidymeadow.co.nz
Slogan: Competitive prices, and personal service in the Kowhai Vale district

The theme is green as its for a lawn mowing outfit!

```html
<!DOCTYPE html>
<html lang="en">
<head>
<meta charset="utf-8">
<title>Tidy Meadow – Business Cards</title>
<link href="https://fonts.googleapis.com/css2?family=Open+Sans:wght@400;600;700&display=swap" rel="stylesheet">
<style>
  :root {
    --leaf: #5f7a1c;
    --leaf-band: #6b8a22;
    --ink: #1d1d1d;
    --ink-soft: #3a3a3a;
    --icon: #6a6a6a;
    --paper: #ffffff;
    --backdrop: #e9e6e1;
    --divider: #8fa35a;
  }
  * { box-sizing: border-box; margin: 0; padding: 0; }
  html, body { width: 1200px; height: 1049px; overflow: hidden; }
  body {
    background: var(--backdrop);
    font-family: "Open Sans", Arial, sans-serif;
    color: var(--ink);
    position: relative;
  }
  .card {
    position: absolute;
    left: 220px;
    width: 760px;
    height: 464px;
    background: var(--paper);
    box-shadow: 0 4px 14px rgba(0,0,0,0.18);
    overflow: hidden;
  }
  .card--back { top: 40px; }
  .card--front { top: 545px; }

  .brand {
    display: flex;
    align-items: center;
    gap: 14px;
    color: var(--leaf);
    font-weight: 700;
    font-size: 40px;
    letter-spacing: 0.5px;
    white-space: nowrap;
  }
  .brand__dot {
    width: 22px; height: 22px;
    border-radius: 50%;
    background: var(--leaf);
    flex: none;
  }

  .card--back .brand { position: absolute; left: 0; right: 0; top: 180px; justify-content: center; }
  .card--back .site {
    position: absolute; left: 0; right: 0; top: 270px;
    text-align: center;
    font-size: 19px;
    color: var(--ink-soft);
  }

  .front__brand-side {
    position: absolute; left: 0; top: 0;
    width: 400px; height: 396px;
    display: flex; align-items: center; justify-content: center;
  }
  .front__brand-side .brand { font-size: 36px; }
  .front__divider {
    position: absolute; left: 400px; top: 30px;
    width: 2px; height: 336px;
    background: linear-gradient(to bottom, rgba(143,163,90,0), var(--divider) 60%, var(--leaf));
  }
  .contact {
    position: absolute; left: 440px; top: 80px; right: 24px;
  }
  .contact__name { font-size: 30px; font-weight: 700; color: var(--ink); line-height: 1.15; }
  .contact__role { font-size: 20px; color: var(--ink-soft); margin-top: 2px; }
  .contact__list { list-style: none; margin-top: 44px; }
  .contact__item {
    display: flex; align-items: center; gap: 10px;
    font-size: 18px; color: var(--ink-soft);
    line-height: 1.35;
    white-space: nowrap;
  }
  .contact__item svg { width: 16px; height: 16px; flex: none; fill: var(--icon); }

  .slogan-band {
    position: absolute; left: 0; right: 0; bottom: 0;
    height: 68px;
    padding: 0 24px;
    background: var(--leaf-band);
    color: #fff;
    display: flex; align-items: center; justify-content: center;
    font-size: 17px; font-weight: 600;
    letter-spacing: 1px;
    text-transform: uppercase;
    white-space: nowrap;
  }
</style>
</head>
<body>

  <section class="card card--back">
    <div class="brand"><span class="brand__dot"></span>Tidy Meadow</div>
    <p class="site">www.tidymeadow.co.nz</p>
  </section>

  <section class="card card--front">
    <div class="front__brand-side">
      <div class="brand"><span class="brand__dot"></span>Tidy Meadow</div>
    </div>
    <div class="front__divider"></div>

    <div class="contact">
      <h1 class="contact__name">Harriet Osbrook</h1>
      <p class="contact__role">Lawn Mowing Services</p>
      <ul class="contact__list">
        <li class="contact__item">
          <svg viewBox="0 0 16 16" aria-hidden="true"><path d="M3.6 1.5l2.3 2.6-1.3 1.9c.9 2 2.4 3.5 4.4 4.4l1.9-1.3 2.6 2.3-1.2 2.3C7 13.6 2.4 9 1.3 2.7z"/></svg>
          0224819357
        </li>
        <li class="contact__item">
          <svg viewBox="0 0 16 16" aria-hidden="true"><path d="M1 3.5h14v9H1zm1.4 1L8 8.7l5.6-4.2z"/></svg>
          harrietosb@tidymeadow.co.nz
        </li>
        <li class="contact__item">
          <svg viewBox="0 0 16 16" aria-hidden="true"><path d="M8 1a7 7 0 100 14A7 7 0 008 1zm0 1.4c.8.8 1.4 2.2 1.6 4H6.4C6.6 4.6 7.2 3.2 8 2.4zm-1.6 5.2h3.2c-.2 1.8-.8 3.2-1.6 4-.8-.8-1.4-2.2-1.6-4zM2.5 6.4h2.7c.1-1.5.5-2.8 1-3.7a5.6 5.6 0 00-3.7 3.7zm0 1.2a5.6 5.6 0 003.7 3.7c-.5-.9-.9-2.2-1-3.7zm8.3 0c-.1 1.5-.5 2.8-1 3.7a5.6 5.6 0 003.7-3.7zm0-1.2h2.7a5.6 5.6 0 00-3.7-3.7c.5.9.9 2.2 1 3.7z"/></svg>
          www.tidymeadow.co.nz
        </li>
      </ul>
    </div>

    <div class="slogan-band">Competitive prices, and personal service in the Kowhai Vale district</div>
  </section>

</body>
</html>
```